Mortgage Broking boutique Business

I’m wanting a revamped look to my existing business card design. I do like the black and silver but happy to have other colours introduced based on your creation. I’ve attached a copy of my current card so you can have a starting point updated details noted brloe. I deal with high net worth individuals so need my card to be sophisticated, classy that gives off a classy vibe

Target Market(s)

High net worth, wealthy

Industry/Entity Type

Mortgage Brokerage

Contact Information for Business Card

Job title: Finance Executive
Phone: +61 7 3862 1197
Mobile: 0431 275 506
Email: marcus@quillbrookcapital.com.au
Web: www.quillbrookcapital.com.au
Address: level 22 Tamberlin House, 48 Mercer Rd Brisbane QLD 4000

Font styles to use
Other font styles liked:
• Helvetica

Colors

Designer to choose colors to be used in the design.

Requirements
Must have
• Use my existing card design as a starting point

```html
<!DOCTYPE html>
<html lang="en">
<head>
<meta charset="utf-8">
<title>Quillbrook Capital – Business Cards</title>
<link href="https://fonts.googleapis.com/css2?family=Jost:wght@300;400&family=Open+Sans:wght@400;700&display=swap" rel="stylesheet">
<style>
  :root {
    --canvas: #2a2d31;
    --card-white: #ffffff;
    --card-dark: #2b2828;
    --card-darker: #141313;
    --silver: #9a9a9a;
    --silver-light: #c9c9c9;
    --ink: #1d1d1d;
    --muted: #7c7c7c;
    --text-light: #f2f2f2;
  }
  * { margin: 0; padding: 0; box-sizing: border-box; }
  html, body { width: 1200px; height: 900px; overflow: hidden; }
  body {
    background: var(--canvas);
    font-family: "Jost", Helvetica, Arial, sans-serif;
    position: relative;
  }
  .card {
    position: absolute;
    width: 540px;
    height: 310px;
    border-radius: 22px;
    overflow: hidden;
    box-shadow: 0 18px 40px rgba(0,0,0,.45);
  }
  /* Front */
  .card--front { left: 40px; top: 295px; background: var(--card-white); }
  .card__edge { position: absolute; left: 0; bottom: 0; width: 540px; height: 310px; }
  .brand { position: absolute; left: 34px; top: 28px; color: var(--ink); text-align: center; }
  .brand__name { font-weight: 300; font-size: 26px; letter-spacing: 7px; line-height: 1; }
  .brand__sub { font-weight: 300; font-size: 12px; letter-spacing: 5px; margin-top: 6px; }
  .person { position: absolute; left: 34px; top: 118px; }
  .person__name { font-family: "Open Sans", Helvetica, Arial, sans-serif; font-weight: 700; font-size: 19px; color: var(--ink); }
  .person__title {
    font-family: "Open Sans", Helvetica, Arial, sans-serif; font-size: 11px; color: var(--muted);
    border-top: 1px solid var(--silver); margin-top: 4px; padding-top: 3px; width: 150px;
  }
  .divider { position: absolute; left: 230px; top: 108px; width: 1px; height: 120px; background: var(--silver-light); }
  .contacts { position: absolute; left: 252px; top: 100px; list-style: none; }
  .contacts li {
    display: flex; align-items: flex-start; gap: 9px;
    font-size: 13px; font-weight: 400; color: var(--muted); line-height: 1.35; margin-bottom: 4px;
  }
  .contacts svg { flex: none; width: 13px; height: 13px; margin-top: 2px; }
  /* Back */
  .card--back {
    left: 620px; top: 295px;
    background: linear-gradient(100deg, #3a3636 0%, var(--card-dark) 55%, var(--card-darker) 100%);
  }
  .card--back .band {
    position: absolute; right: 0; top: 0; width: 110px; height: 100%;
    background: linear-gradient(90deg, rgba(0,0,0,.25), rgba(0,0,0,.45));
  }
  .back-brand { position: absolute; left: 0; right: 110px; top: 92px; text-align: center; color: var(--text-light); }
  .back-brand__name { font-weight: 300; font-size: 40px; letter-spacing: 10px; line-height: 1; }
  .back-brand__sub { font-weight: 300; font-size: 16px; letter-spacing: 8px; margin-top: 10px; }
  .back-web { position: absolute; left: 0; right: 110px; top: 228px; text-align: center; color: var(--text-light); font-size: 15px; letter-spacing: .5px; }
</style>
</head>
<body>

<section class="card card--front">
  <svg class="card__edge" viewBox="0 0 540 310" aria-hidden="true">
    <polyline points="0,226 200,226 270,268 340,226 540,226" fill="none" stroke="var(--silver-light)" stroke-width="5"/>
    <polyline points="0,236 200,236 270,278 340,236 540,236" fill="none" stroke="var(--silver)" stroke-width="5"/>
    <polygon points="0,246 200,246 270,288 340,246 540,246 540,310 0,310" fill="var(--card-dark)"/>
  </svg>

  <div class="brand">
    <div class="brand__name">QUILLBROOK</div>
    <div class="brand__sub">CAPITAL</div>
  </div>

  <div class="person">
    <div class="person__name">Example Name</div>
    <div class="person__title">Finance Executive</div>
  </div>

  <div class="divider"></div>

  <ul class="contacts">
    <li>
      <svg viewBox="0 0 13 13"><rect width="13" height="13" rx="2" fill="var(--silver)"/><path d="M6.5 2.5a2.6 2.6 0 0 0-2.6 2.6c0 2 2.6 5 2.6 5s2.6-3 2.6-5a2.6 2.6 0 0 0-2.6-2.6z" fill="#fff"/></svg>
      <span>level 22 Tamberlin House,<br>48 Mercer Rd Brisbane QLD 4000</span>
    </li>
    <li>
      <svg viewBox="0 0 13 13"><rect width="13" height="13" rx="2" fill="var(--silver)"/><path d="M4 3h2l.8 2-1.2.8a5 5 0 0 0 1.6 1.6L8 6.2l2 .8v2c0 .6-.5 1-1 1A6 6 0 0 1 3 4c0-.5.4-1 1-1z" fill="#fff"/></svg>
      <span>+61 7 3862 1197</span>
    </li>
    <li>
      <svg viewBox="0 0 13 13"><rect width="13" height="13" rx="2" fill="var(--silver)"/><rect x="4.3" y="2.5" width="4.4" height="8" rx="1" fill="#fff"/></svg>
      <span>0431 275 506</span>
    </li>
    <li>
      <svg viewBox="0 0 13 13"><rect width="13" height="13" rx="2" fill="var(--silver)"/><rect x="2.5" y="4" width="8" height="5.5" fill="#fff"/><polyline points="2.5,4 6.5,7 10.5,4" fill="none" stroke="var(--silver)" stroke-width="1"/></svg>
      <span>marcus@quillbrookcapital.com.au</span>
    </li>
    <li>
      <svg viewBox="0 0 13 13"><rect width="13" height="13" rx="2" fill="var(--silver)"/><circle cx="6.5" cy="6.5" r="3.8" fill="none" stroke="#fff" stroke-width="1"/><path d="M2.7 6.5h7.6M6.5 2.7c-2 2.3-2 5.3 0 7.6M6.5 2.7c2 2.3 2 5.3 0 7.6" fill="none" stroke="#fff" stroke-width=".8"/></svg>
      <span>www.quillbrookcapital.com.au</span>
    </li>
  </ul>
</section>

<section class="card card--back">
  <div class="band"></div>
  <div class="back-brand">
    <div class="back-brand__name">QUILLBROOK</div>
    <div class="back-brand__sub">CAPITAL</div>
  </div>
  <div class="back-web">www.quillbrookcapital.com.au</div>
</section>

</body>
</html>
```